Threshold
Business cards/letter head
Threshold - Consulting
Creative Brief
Use standard fonts
Maren Holt
3187 Wexbury Ave NE Seattle, WA 98115
Holt.maren@quillpost.example
please use a complementary font to the logo. logo art uploaded.

```html
<!DOCTYPE html>
<html lang="en">
<head>
<meta charset="utf-8">
<title>Threshold – Business Card</title>
<link rel="stylesheet" href="https://fonts.googleapis.com/css2?family=Jost:wght@300;400&display=swap">
<style>
  :root {
    --page-bg: #e9e7e3;
    --card-white: #ffffff;
    --band-charcoal: #4a4a4c;
    --accent-yellow: #e3c62a;
    --text-grey: #555558;
    --text-dark: #3a3a3c;
  }
  * { margin: 0; padding: 0; box-sizing: border-box; }
  html, body {
    width: 1200px;
    height: 904px;
    overflow: hidden;
    background: var(--page-bg);
    font-family: "Jost", "Futura", sans-serif;
  }
  .business-card {
    position: absolute;
    left: 100px;
    top: 166px;
    width: 1000px;
    height: 572px;
    background: var(--card-white);
    overflow: hidden;
    box-shadow: 0 6px 24px rgba(0,0,0,0.18);
  }
  .card-bands {
    position: absolute;
    inset: 0;
    width: 100%;
    height: 100%;
  }
  .band-dark { fill: var(--band-charcoal); }
  .band-accent { fill: var(--accent-yellow); }
  .holder-name {
    position: absolute;
    right: 70px;
    top: 58px;
    font-size: 27px;
    font-weight: 400;
    color: var(--accent-yellow);
  }
  .brand {
    position: absolute;
    left: 74px;
    top: 318px;
    display: flex;
    align-items: center;
    gap: 18px;
    color: var(--text-grey);
  }
  .brand-mark {
    width: 30px;
    height: 30px;
    border-radius: 50%;
    background: var(--text-grey);
    flex: none;
  }
  .brand-name {
    font-size: 64px;
    font-weight: 300;
    line-height: 1;
    letter-spacing: 1px;
  }
  .address {
    position: absolute;
    left: 96px;
    top: 458px;
    font-size: 20px;
    line-height: 1.3;
    color: var(--text-dark);
    font-style: normal;
  }
  .contact-list {
    position: absolute;
    right: 64px;
    top: 358px;
    list-style: none;
    font-size: 19px;
    line-height: 1.45;
    color: var(--text-dark);
  }
  .contact-list li { display: flex; align-items: center; gap: 10px; }
  .contact-icon { width: 18px; height: 18px; flex: none; }
  .contact-icon * { fill: none; stroke: var(--accent-yellow); stroke-width: 2; }
</style>
</head>
<body>
  <section class="business-card">
    <svg class="card-bands" viewBox="0 0 1000 572" preserveAspectRatio="none" aria-hidden="true">
      <path class="band-dark" d="M0,0 H1000 V118 Q560,88 0,236 Z"/>
      <path class="band-accent" d="M0,248 Q560,100 1000,132 V168 Q560,116 0,256 Z"/>
    </svg>

    <p class="holder-name">Maren Holt</p>

    <div class="brand">
      <span class="brand-mark"></span>
      <span class="brand-name">Threshold</span>
    </div>

    <address class="address">
      3187 Wexbury Ave NE<br>
      Seattle, WA 98115
    </address>

    <ul class="contact-list">
      <li>
        <svg class="contact-icon" viewBox="0 0 18 18" aria-hidden="true"><rect x="4" y="1" width="10" height="16" rx="2"/></svg>
        +1 206 555-0142
      </li>
      <li>
        <svg class="contact-icon" viewBox="0 0 18 18" aria-hidden="true"><rect x="1" y="4" width="16" height="11"/><path d="M1,4 L9,10 L17,4"/></svg>
        Holt.maren@quillpost.example
      </li>
    </ul>
  </section>
</body>
</html>
```